Wholesale e-commerce website re-design

We are a wholesaler of African-made and African-themed products, and we're looking to update the look and feel of our website www.terramarketgoods.com to improve user experience. We'd like to have a cleaner homepage that keeps the product category menus (but simplifies them), allows certain products to be featured, and has a simple CTA box (something like "Login" for existing wholesale customers or "Start a Business" for new customers). The layout might be something along the lines of http://www.pinewillowwares.com/ except with a shopping cart featured at the top right. Our colors tend to be earth-toned, but the current color palate looks dated. Also see our blog.terramarketgoods.com page for themes and color ideas that are maybe more up-to-date. On our product pages, we want to feature the products more prominently and have simpler, cleaner Buy or Add buttons.

Other reference sites for inspiration: vastherbalcrate.com, cozykitchenry.com, http://www.pinewillowwares.com, http://mbelatraders.com/ http://orunesa.com/

Reason: We like many of the designs that have been submitted so far, but need more time to make our final choice.

Target Market(s)

Small wholesale customers, most have a small business or home-based business. Also some retail, so an option for retail customers to click at the top to see retail pricing would be nice

Industry/Entity Type

Wholesale

Number of Pages Required

3 page

Font styles to use
Sans Serif

Requirements
Must have
• Clean, clear design that highlights products and reduces friction to customer purchase. Should include one homepage, one product page, and one shopping cart page design. Works with all browser types and be mobile-friendly.
Nice to have
• Other color schemes that would look good with our logo (maybe different from colors chosen below).
Should not have
• Splash pages with special effects, Adobe flash, elements that slow down page load times or that only work well in certain browsers.

```html
<!DOCTYPE html>
<html lang="en">
<head>
<meta charset="utf-8">
<title>Terra Market Goods — Home</title>
<link href="https://fonts.googleapis.com/css2?family=Raleway:wght@400;500;600;700&family=Playfair+Display:ital,wght@0,700;1,700;1,900&display=swap" rel="stylesheet">
<style>
:root{
  --ink:#1f1f1f;
  --dark:#222325;
  --darker:#141414;
  --red:#e5342b;
  --gold:#e8a321;
  --gold-box:rgba(196,140,60,.82);
  --grey:#8a8a8a;
  --line:#d8d8d8;
  --white:#ffffff;
  --sans:'Raleway', Arial, sans-serif;
  --serif:'Playfair Display', Georgia, serif;
}
*{margin:0;padding:0;box-sizing:border-box}
html,body{width:1200px;height:2528px;overflow:hidden;background:var(--white);font-family:var(--sans);color:var(--ink)}
.page{position:relative;width:1200px;height:2528px;overflow:hidden}
.abs{position:absolute}

/* top bar */
.topbar{left:0;top:0;width:1200px;height:17px;background:var(--darker);color:#ddd;font-size:8px;display:flex;justify-content:flex-end;align-items:center;gap:14px;padding-right:20px}
.topbar .sep{color:#777}

/* header */
.header{left:0;top:17px;width:1200px;height:106px;background:var(--white)}
.brand{left:100px;top:12px;width:86px;height:86px;display:flex;align-items:center;gap:6px}
.brand .mark{width:12px;height:12px;background:var(--red);border-radius:50%;flex:none}
.brand .name{font-size:13px;font-weight:700;color:var(--red);line-height:1.05;text-transform:uppercase}
.mainnav{left:224px;top:16px;display:flex;gap:26px;font-size:10px;font-weight:600;text-transform:uppercase;letter-spacing:.4px}
.mainnav .active{border-bottom:2px solid var(--red);padding-bottom:3px}
.search{left:222px;top:39px;width:586px;height:24px;display:flex}
.search .field{flex:1;border:1px solid var(--line);font-size:8px;color:var(--grey);padding:7px 8px}
.search .select{width:108px;border:1px solid var(--line);border-left:none;font-size:8px;color:#555;padding:7px 8px;position:relative}
.search .select::after{content:"";position:absolute;right:8px;top:9px;border:3px solid transparent;border-top-color:#555}
.search .btn{width:100px;margin-left:6px;background:var(--red);color:var(--white);font-size:9px;font-weight:700;display:flex;align-items:center;justify-content:center;gap:6px}
.catnav{left:224px;top:80px;display:flex;gap:15px;font-size:8px;color:#333}
.catnav span::after{content:" ▾";font-size:6px}
.account{left:934px;top:14px;display:flex;gap:26px;font-size:9px;color:var(--grey);align-items:center}
.cart{display:flex;align-items:center;gap:5px}
.badge{width:15px;height:15px;border-radius:50%;background:var(--gold);color:var(--white);font-size:8px;display:flex;align-items:center;justify-content:center}
.help{left:958px;top:40px;width:140px;height:38px;background:linear-gradient(90deg,#3a4a5e,#6a7c92 60%,#c79f82);color:var(--white);font-size:10px;font-weight:700;line-height:1.05;padding:4px 6px}
.social{left:998px;top:86px;display:flex;gap:10px}
.social i{width:8px;height:8px;border-radius:50%;background:var(--gold);display:block}

/* quick bar */
.quickbar{left:0;top:123px;width:1200px;height:21px;background:var(--gold);color:var(--white);font-size:8px;display:flex;align-items:center;padding-left:224px;gap:10px}

/* hero */
.hero{left:0;top:144px;width:1200px;height:516px;background:radial-gradient(ellipse at 30% 40%,#c85a32,#8a3a22 40%,#5a3424 70%,#3a2a22)}
.hero .eyebrow{left:0;top:196px;width:1200px;text-align:center;color:var(--white);font-size:10px;letter-spacing:2px}
.hero h1{left:0;top:236px;width:1200px;text-align:center;color:var(--white);font-size:30px;font-weight:400;letter-spacing:3px}
.hero .cta{left:542px;top:306px;width:116px;height:28px;background:var(--red);color:var(--white);font-size:8px;font-weight:700;display:flex;align-items:center;justify-content:center}
.hero svg{position:absolute;top:240px}

/* shipping */
.shipping{left:0;top:660px;width:1200px;height:99px;background:var(--dark);text-align:center;color:var(--gold)}
.shipping h2{margin-top:12px;font-size:16px;font-weight:700;letter-spacing:.5px}
.shipping p{font-size:7.5px;line-height:1.6;width:560px;margin:6px auto 0}
.dots{left:1164px;top:22px;display:flex;flex-direction:column;gap:7px}
.dots i{width:7px;height:7px;border-radius:50%;background:#888;display:block}
.dots i:first-child{background:var(--white)}

/* tiles */
.tile{overflow:hidden}
.photo{position:absolute;inset:0}
.tile .label{position:absolute;color:var(--white);font-size:8.5px;font-weight:600;text-transform:uppercase;letter-spacing:.3px}
.tile .label::after{content:"";display:block;width:22px;height:1px;background:var(--white);margin-top:8px}
.tile .title{position:absolute;color:var(--white);font-family:var(--serif);font-style:italic;font-weight:900;font-size:20px;line-height:1.1}
.tile .explore{position:absolute;width:80px;height:26px;background:var(--gold);color:var(--white);font-size:7px;font-weight:700;display:flex;align-items:center;justify-content:center}
.tile.light .heading{position:absolute;left:0;width:100%;text-align:center;font-size:8.5px;font-weight:700;text-transform:uppercase}
.price{position:absolute;font-family:var(--serif);font-style:italic;font-weight:700;color:var(--gold);font-size:15px}
.box{position:absolute;background:var(--gold-box);text-align:center;color:var(--white)}
.box .label{position:static;display:block;margin-top:22px}
.box .label::after{margin:8px auto 0}
.box .big{font-family:var(--serif);font-style:italic;font-weight:900;font-size:38px;line-height:1;margin-top:18px}

/* products */
.tabs{left:0;top:1544px;width:1200px;display:flex;justify-content:center;gap:0;font-size:10px;font-weight:700;text-transform:uppercase}
.tabs span{display:block;text-align:center}
.tabs .on{border-bottom:2px solid var(--red);padding-bottom:6px}
.product .img{position:absolute;border:2px solid var(--line)}
.product .img div{position:absolute;inset:12px}
.product .pname{position:absolute;font-size:10px;font-weight:700}
.product .pcost{position:absolute;font-size:10px;font-weight:600;text-align:right}
.product .psub{position:absolute;font-size:6.5px;color:var(--grey);text-transform:uppercase}
.product .buy{position:absolute;width:18px;height:10px;background:var(--red);color:var(--white);font-size:5.5px;font-weight:700;display:flex;align-items:center;justify-content:center}
.featured{left:200px;top:1586px;width:200px;height:431px;background:var(--white);box-shadow:0 2px 14px rgba(0,0,0,.18)}
.featured .img{position:absolute;left:14px;top:22px;width:172px;height:240px}
.thumbs{position:absolute;left:16px;top:278px;display:flex;gap:4px}
.thumbs i{width:24px;height:44px;display:block}
.arrow{position:absolute;width:24px;height:24px;border-radius:50%;background:var(--gold);top:288px;display:flex;align-items:center;justify-content:center}
.featured .pname{left:18px;top:348px}
.featured .pcost{right:20px;top:348px}
.featured .psub{left:18px;top:366px}
.stars{position:absolute;right:20px;top:364px;color:var(--gold);font-size:8px;letter-spacing:1px}
.addbag{position:absolute;left:16px;top:392px;width:168px;height:24px;background:var(--red);color:var(--white);font-size:7.5px;font-weight:700;display:flex;align-items:center;justify-content:center}

/* newsletter */
.newsletter{left:0;top:2276px;width:1200px;height:108px;text-align:center}
.newsletter h3{margin-top:22px;font-size:15px;font-weight:700}
.newsletter .form{display:flex;justify-content:center;gap:10px;margin-top:16px}
.newsletter .email{width:290px;height:31px;border:1px solid #bbb;font-size:7px;color:var(--grey);text-align:left;padding:11px 8px}
.newsletter .sub{width:100px;height:31px;background:var(--red);color:var(--white);font-size:8.5px;font-weight:700;display:flex;align-items:center;justify-content:center}

/* footer */
.footer{left:0;top:2384px;width:1200px;height:144px;background:var(--dark);color:#ddd;text-align:center}
.footer .fbrand{margin:14px auto 0;display:flex;align-items:center;justify-content:center;gap:6px;color:var(--white);font-size:11px;font-weight:700;text-transform:uppercase}
.footer .fbrand i{width:10px;height:10px;border-radius:50%;background:var(--white);display:block}
.footer .fsocial{display:flex;justify-content:center;gap:14px;margin-top:26px}
.footer .fsocial i{width:8px;height:8px;border-radius:50%;background:var(--white);display:block}
.footer .fnav{display:flex;justify-content:center;gap:16px;margin-top:12px;font-size:7.5px}
.footer .fnav span::after{content:" ▾";font-size:5px}
.footer .copy{margin-top:8px;font-size:6.5px;color:#999}
</style>
</head>
<body>
<div class="page">

  <div class="abs topbar">
    <span>Tel: (555) 014-2280</span><span class="sep">|</span>
    <span>Fax: (555) 014-2291</span><span class="sep">|</span>
    <span>contact@terramarketgoods.com</span>
  </div>

  <header class="abs header">
    <div class="abs brand" style="top:0"><span class="mark"></span><span class="name">Terra<br>Market<br>Goods</span></div>
    <nav class="abs mainnav"><span class="active">Home</span><span>Shop</span><span>Categories ▾</span><span>About</span><span>Contact</span></nav>
    <div class="abs search">
      <div class="field">Search keywords or items #</div>
      <div class="select">All categories</div>
      <div class="btn">
        <svg width="9" height="9" viewBox="0 0 10 10"><circle cx="4" cy="4" r="3" fill="none" stroke="#fff" stroke-width="1.5"/><line x1="6.2" y1="6.2" x2="9" y2="9" stroke="#fff" stroke-width="1.5"/></svg>
        SEARCH
      </div>
    </div>
    <nav class="abs catnav">
      <span>African Clothing</span><span>African Fabrics</span><span>African Soaps</span><span>Oils, Incense &amp; Burners</span><span>Health &amp; Beauty</span><span>Jewelry</span><span>Miscellaneous</span><span>Musical Instruments</span><span>Artwork</span>
    </nav>
    <div class="abs account">
      <span>Sign Up</span><span>Login</span>
      <span class="cart">
        <svg width="12" height="12" viewBox="0 0 12 12"><path d="M2 4h8l-1 7H3z" fill="none" stroke="#333" stroke-width="1.2"/><path d="M4 4V3a2 2 0 0 1 4 0v1" fill="none" stroke="#333" stroke-width="1.2"/></svg>
        Cart <span class="badge">0</span>
      </span>
    </div>
    <div class="abs help" role="img" aria-label="Live help banner with support agent photo">Need Help?<br>Click Here for<br>Live Help</div>
    <div class="abs social"><i></i><i></i><i></i><i></i><i></i></div>
  </header>

  <div class="abs quickbar">
    <span>New Items</span><span>|</span><span>Item Quick Order</span><span>|</span><span>Top 10 Best sellers</span><span>|</span><span>Web Specials</span><span>|</span><span>Promotions</span>
  </div>

  <section class="abs hero">
    <div class="photo" role="img" aria-label="Stacked colourful woven baskets"></div>
    <div class="abs eyebrow">ACCESSORIES</div>
    <h1 class="abs">AFRICA CLOTHING BASKETS</h1>
    <div class="abs cta">DISCOVER MORE</div>
    <svg style="left:38px" width="16" height="12" viewBox="0 0 16 12"><path d="M15 6H2M6 2 2 6l4 4" fill="none" stroke="#fff" stroke-width="1.6"/></svg>
    <svg style="left:1148px" width="16" height="12" viewBox="0 0 16 12"><path d="M1 6h13M10 2l4 4-4 4" fill="none" stroke="#fff" stroke-width="1.6"/></svg>
  </section>

  <section class="abs shipping">
    <h2>SAME DAY SHIPPING</h2>
    <p>ORDER BEFORE 2 PM (EST) TO SHIP YOUR ORDER TODAY! (US MAIL ORDERS WILL BE SHIPPED THE SAME DAY BEFORE 11:30 AM) ESPECIALLY LARGE ORDERS PLACED AFTER NOON MAY BE SENT ON THE FOLLOWING DAY.<br>NO SHIPMENTS ARE SENT ON SATURDAY, SUNDAY, OR HOLIDAYS.<br>ORDERS CAN NOT BE CHANGED OR ADDED TO ON THE DAY THEY ARE BEING SHIPPED.</p>
    <div class="abs dots"><i></i><i></i><i></i><i></i></div>
  </section>

  <!-- row 1 -->
  <div class="abs tile" style="left:0;top:759px;width:513px;height:249px">
    <div class="photo" role="img" aria-label="Shea butter, nuts and bowls on a table" style="background:linear-gradient(120deg,#2a2420,#5a4634 45%,#8a6a48 70%,#3a2e24)"></div>
    <span class="label" style="left:63px;top:44px">Health</span>
    <span class="title" style="left:63px;top:100px">Health<br>&amp; Beauty</span>
    <span class="explore" style="left:63px;top:179px">EXPLORE</span>
  </div>
  <div class="abs tile light" style="left:513px;top:759px;width:342px;height:249px">
    <span class="heading" style="top:38px">Men's Brocade Dashiki</span>
    <span class="price" style="left:140px;top:74px">$19,99</span>
    <div class="abs" role="img" aria-label="Two men wearing brocade dashikis" style="left:90px;top:92px;width:160px;height:157px;background:linear-gradient(90deg,#6a4a9a,#7a5a3a)"></div>
  </div>
  <div class="abs tile" style="left:855px;top:759px;width:345px;height:249px">
    <div class="photo" role="img" aria-label="Traditional drums at a market" style="background:linear-gradient(135deg,#6a3a3a,#9a6a5a 50%,#5a3a34)"></div>
    <div class="box" style="left:73px;top:24px;width:200px;height:205px">
      <span class="label">Musical Instruments</span>
      <div class="big">%20<br>Sale</div>
    </div>
  </div>

  <!-- row 2 -->
  <div class="abs tile light" style="left:0;top:1008px;width:342px;height:252px">
    <span class="heading" style="top:26px">Traditional Print Stretch Shirt</span>
    <span class="price" style="left:158px;top:44px">$19.99</span>
    <div class="abs" role="img" aria-label="Two women wearing print stretch shirts" style="left:80px;top:66px;width:180px;height:186px;background:linear-gradient(90deg,#f07a2a,#3a9a4a)"></div>
  </div>
  <div class="abs tile" style="left:342px;top:1008px;width:347px;height:252px">
    <div class="photo" role="img" aria-label="Roasted coffee beans" style="background:linear-gradient(135deg,#2a1a12,#6a4228 50%,#3a2418)"></div>
    <div class="box" style="left:72px;top:29px;width:198px;height:223px">
      <span class="label">In Coffee</span>
      <div class="big" style="font-size:30px;margin-top:22px">This<br>Week</div>
    </div>
  </div>
  <div class="abs tile" style="left:689px;top:1008px;width:511px;height:252px">
    <div class="photo" role="img" aria-label="Stacks of colourful African print fabric" style="background:linear-gradient(135deg,#a02a2a,#d86a2a 30%,#4a3a8a 55%,#c83a3a 80%,#6a2a2a)"></div>
    <span class="label" style="left:64px;top:44px">Luxury Print Fabric</span>
    <span class="title" style="left:64px;top:100px">Luxury Collection<br>African Fabric</span>
    <span class="explore" style="left:64px;top:188px">EXPLORE</span>
  </div>

  <!-- row 3 -->
  <div class="abs tile" style="left:0;top:1260px;width:513px;height:249px">
    <div class="photo" role="img" aria-label="Woven thatched roof interior of the Kasubi tombs" style="background:radial-gradient(ellipse at 60% 50%,#a85a28,#6a2e14 50%,#2a140a)"></div>
    <span class="label" style="left:63px;top:44px">Tombeaux, Ouganda</span>
    <span class="title" style="left:63px;top:100px">Kasubi,<br>Afrique</span>
    <span class="explore" style="left:63px;top:180px">EXPLORE</span>
  </div>
  <div class="abs tile" style="left:513px;top:1260px;width:342px;height:249px">
    <div class="photo" role="img" aria-label="Two women in colourful kaftans" style="background:linear-gradient(90deg,#e8e4de,#b8483a 40%,#3a5a8a 70%,#e8e4de)"></div>
    <div class="box" style="left:104px;top:15px;width:170px;height:205px">
      <span class="label">New Arrivals</span>
      <div class="big">%5<br>Sale</div>
    </div>
  </div>
  <div class="abs tile" style="left:855px;top:1260px;width:345px;height:249px">
    <div class="photo" role="img" aria-label="Glass bottles of essential oils with flowers" style="background:linear-gradient(135deg,#eef2e0,#9ac25a 40%,#3a7a3a 70%,#6a3a1a)"></div>
    <span class="label" style="left:145px;top:170px">Oil Sets</span>
    <span class="price" style="left:145px;top:206px;font-size:13px">$9,99</span>
  </div>

  <!-- product tabs -->
  <div class="abs tabs">
    <span style="width:200px;margin-left:-1px">All Products</span>
    <span style="width:200px"><span class="on">New Arrivals</span></span>
    <span style="width:200px">Top Sales</span>
    <span style="width:200px">Categories</span>
  </div>

  <!-- product grid -->
  <div class="product">
    <div class="img" style="left:417px;top:1600px;width:166px;height:255px"><div role="img" aria-label="Maasai sword with red sheath" style="background:linear-gradient(90deg,#fff,#c7c2ba 45%,#b02a2a 60%,#fff)"></div></div>
    <span class="pname" style="left:417px;top:1875px">Maasai Sword</span><span class="pcost" style="left:540px;top:1875px;width:43px">$7.29</span>
    <span class="psub" style="left:417px;top:1895px">Maasai Sword</span><span class="buy" style="left:565px;top:1893px">Buy</span>

    <div class="img" style="left:617px;top:1600px;width:167px;height:255px"><div role="img" aria-label="Carved ebony sculpture" style="background:linear-gradient(90deg,#fff,#1a1a1a 40%,#1a1a1a 60%,#fff)"></div></div>
    <span class="pname" style="left:617px;top:1875px">Ebony art</span><span class="pcost" style="left:740px;top:1875px;width:44px">$79</span>
    <span class="psub" style="left:617px;top:1895px">Ebony Art</span><span class="buy" style="left:766px;top:1893px">Buy</span>

    <div class="img" style="left:819px;top:1600px;width:165px;height:255px"><div role="img" aria-label="Eight-string harp guitar" style="background:linear-gradient(180deg,#fff,#d8d2c8 50%,#fff)"></div></div>
    <span class="pname" style="left:819px;top:1875px">Nyatiti 8-String Guitar</span><span class="pcost" style="left:940px;top:1875px;width:44px">$9.95</span>
    <span class="psub" style="left:819px;top:1895px">Nyatiti 8-String Guitar</span><span class="buy" style="left:966px;top:1893px">Buy</span>

    <div class="img" style="left:217px;top:1940px;width:166px;height:254px"><div role="img" aria-label="Silver cuff bracelet" style="background:linear-gradient(180deg,#fff,#d4d4d4 60%,#fff)"></div></div>
    <span class="pname" style="left:218px;top:2217px">Tuareg Round Blk-Etched</span><span class="pcost" style="left:340px;top:2217px;width:43px">$4.95</span>
    <span class="psub" style="left:218px;top:2237px">Tuareg Round Blk-Etched</span><span class="buy" style="left:365px;top:2235px">Buy</span>

    <div class="img" style="left:417px;top:1940px;width:166px;height:254px"><div role="img" aria-label="Two men in embroidered grand boubou" style="background:linear-gradient(90deg,#fff,#3a6a3a 35%,#e8e8e8 65%,#fff)"></div></div>
    <span class="pname" style="left:417px;top:2217px">Grand BouBou</span><span class="pcost" style="left:533px;top:2217px;width:50px">$64.95</span>
    <span class="psub" style="left:417px;top:2237px">Embroidered Grand Boubou</span><span class="buy" style="left:565px;top:2235px">Buy</span>

    <div class="img" style="left:617px;top:1940px;width:167px;height:254px"><div role="img" aria-label="Bar of black soap on a wooden dish" style="background:linear-gradient(180deg,#2a2a2a,#2a2a2a 30%,#c8d8c0 50%,#b88a5a 80%,#fff)"></div></div>
    <span class="pname" style="left:617px;top:2217px">Aloe Vera Soap - 4½ oz.</span><span class="pcost" style="left:740px;top:2217px;width:44px">$1.95</span>
    <span class="psub" style="left:617px;top:2237px">Aloe Vera Soap - 4½ oz.</span><span class="buy" style="left:766px;top:2235px">Buy</span>

    <div class="img" style="left:819px;top:1940px;width:165px;height:254px"><div role="img" aria-label="Jar of hair pomade" style="background:linear-gradient(180deg,#fff,#3a6a2a 25%,#7a3a14 55%,#5a2a10 80%,#fff)"></div></div>
    <span class="pname" style="left:819px;top:2217px">Aloe Vera Hair Pomade</span><span class="pcost" style="left:940px;top:2217px;width:44px">$3.95</span>
    <span class="psub" style="left:819px;top:2237px">Aloe Vera Hair Pomade</span><span class="buy" style="left:966px;top:2235px">Buy</span>
  </div>

  <div class="abs featured product">
    <div class="img" role="img" aria-label="Two women wearing print summer hats" style="border:none;background:linear-gradient(180deg,#fff,#c85a2a 30%,#1a1a1a 65%,#fff)"></div>
    <div class="thumbs">
      <i role="img" aria-label="Print top thumbnail" style="background:#c84a2a"></i>
      <i role="img" aria-label="Print top thumbnail" style="background:#3a3a6a"></i>
      <i role="img" aria-label="Print top thumbnail" style="background:#d86a3a"></i>
      <i role="img" aria-label="Print top thumbnail" style="background:#7a4a8a"></i>
      <i role="img" aria-label="Print top thumbnail" style="background:#3a7aaa"></i>
      <i role="img" aria-label="Print top thumbnail" style="background:#c83a4a"></i>
    </div>
    <span class="arrow" style="left:-12px"><svg width="8" height="8" viewBox="0 0 8 8"><path d="M5 1 2 4l3 3" fill="none" stroke="#fff" stroke-width="1.5"/></svg></span>
    <span class="arrow" style="left:188px"><svg width="8" height="8" viewBox="0 0 8 8"><path d="M3 1l3 3-3 3" fill="none" stroke="#fff" stroke-width="1.5"/></svg></span>
    <span class="pname">African Hat Summer</span><span class="pcost">$26</span>
    <span class="psub">Tops &amp; More</span><span class="stars">★★★★★</span>
    <span class="addbag">ADD TO BAG</span>
  </div>

  <section class="abs newsletter">
    <h3>Stay update with latest news and discounts</h3>
    <div class="form"><div class="email">Email Address</div><div class="sub">SUBSCRIBE</div></div>
  </section>

  <footer class="abs footer">
    <div class="fbrand"><i></i>Terra Market Goods</div>
    <div class="fsocial"><i></i><i></i><i></i><i></i><i></i></div>
    <nav class="fnav"><span>African Clothing</span><span>African Fabrics</span><span>African Soaps</span><span>Oils, Incense &amp; Burners</span><span>Health &amp; Beauty</span><span>Jewelry</span><span>Miscellaneous</span><span>Musical Instruments</span><span>Artwork</span></nav>
    <div class="copy">© 2016 Copyright Terra Market Goods</div>
  </footer>

</div>
</body>
</html>
```